Employee I.D. Card - Badge

We need an employee I.D. card designed. Our employees are going to be wearing these. I would like to have it look nice. Something professional yet cool (not uptight if that makes sense).
Project Scope:
Vertical orientation
Company name ------------- (Bright and Tidy)
Website ------------- (brightandtidymn.example)
Employee Picture
background check image
front and back designed - same design on either side
You can create the card without having the employee images on them.
Here are the dimensions -
2.125 x 3.370 inches
Double sided - same design can be used front and back
Background badge - I would like to add an image that shows that the employee has taken a background check. I've added the press-kit for the company we use. If you have a better idea than incorporating their logo, we can certainly do something different.
Example image-
https://www.findwell-search.example/results?q=background+check+badge&mode=images
The print company will set up the names.
Logo is attached
Also attached are our business cards. You can use this for an idea of brand/company style.
Our website - brightandtidymn.example

```html
<!DOCTYPE html>
<html lang="en">
<head>
<meta charset="utf-8">
<title>Bright and Tidy – Employee ID Badge</title>
<link rel="stylesheet" href="https://fonts.googleapis.com/css2?family=Work+Sans:wght@400;500&display=swap">
<style>
  :root {
    --page-bg: #e0e1e1;
    --card-bg: #ffffff;
    --blue-light: #00b3ef;
    --blue-dark: #0b6fb6;
    --green-light: #8cc63f;
    --green-bright: #c8dc2a;
    --text-white: #ffffff;
    --text-grey: #555a5e;
    --brand-blue: #1494d6;
    --seal-gold: #d8b25a;
    --seal-dark: #1d1d1b;
  }
  * { margin: 0; padding: 0; box-sizing: border-box; }
  html, body {
    width: 1200px; height: 992px; overflow: hidden;
    background: var(--page-bg);
    font-family: "Work Sans", Arial, sans-serif;
  }
  .badge {
    position: absolute; top: 158px;
    width: 425px; height: 675px;
    border-radius: 38px; overflow: hidden;
    background: var(--card-bg);
    box-shadow: 0 14px 30px rgba(0,0,0,.22);
  }
  .badge--front { left: 143px; }
  .badge--back { left: 629px; }
  .badge__art { position: absolute; inset: 0; width: 425px; height: 675px; }
  .badge__name {
    position: absolute; top: 44px; width: 100%; text-align: center;
    color: var(--text-white); font-size: 31px; font-weight: 400;
    letter-spacing: 3.5px;
  }
  .badge__role {
    position: absolute; top: 83px; width: 100%; text-align: center;
    color: var(--text-white); font-size: 22px; font-weight: 400;
  }
  .badge__website {
    position: absolute; top: 484px; width: 100%; text-align: center;
    color: var(--text-grey); font-size: 22px; letter-spacing: .4px;
  }
  .badge__brand {
    position: absolute; left: 40px; top: 560px; width: 190px;
    display: flex; align-items: center; gap: 10px;
    color: var(--brand-blue); font-size: 30px; font-weight: 500; line-height: 1.05;
  }
  .badge__brand-dot {
    flex: none; width: 12px; height: 12px; border-radius: 50%;
    background: var(--brand-blue);
  }
</style>
</head>
<body>

<div class="badge badge--front">
  <svg class="badge__art" viewBox="0 0 425 675">
    <defs>
      <linearGradient id="blueFront" x1="0" x2="1" y1="0" y2="0">
        <stop offset="0" stop-color="var(--blue-light)"/>
        <stop offset="1" stop-color="var(--blue-dark)"/>
      </linearGradient>
      <linearGradient id="greenFront" x1="0" x2="1" y1="0" y2="0">
        <stop offset="0" stop-color="var(--green-light)"/>
        <stop offset="1" stop-color="var(--green-bright)"/>
      </linearGradient>
      <linearGradient id="ringFront" x1="0" x2="1" y1="0" y2="1">
        <stop offset="0" stop-color="var(--blue-light)"/>
        <stop offset="1" stop-color="var(--blue-dark)"/>
      </linearGradient>
    </defs>
    <rect class="band-blue" width="425" height="460" fill="url(#blueFront)"/>
    <path class="band-green" d="M0 370 Q120 395 212 330 Q300 270 425 320 L425 460 L0 460 Z" fill="url(#greenFront)"/>
    <path class="band-white" d="M0 450 Q200 300 425 420 L425 675 L0 675 Z" fill="var(--card-bg)"/>
    <circle class="photo-frame" cx="212" cy="300" r="142" fill="var(--card-bg)"/>
    <circle class="photo-ring" cx="212" cy="300" r="136" fill="url(#ringFront)"/>
    <circle class="photo-slot" cx="212" cy="300" r="120" fill="#d9d9d9" role="img" aria-label="Employee portrait photo"/>
    <g class="check-seal" role="img" aria-label="Background check cleared seal">
      <circle cx="342" cy="605" r="42" fill="var(--seal-gold)"/>
      <circle cx="342" cy="605" r="33" fill="var(--seal-dark)"/>
    </g>
  </svg>
  <div class="badge__name">DANA MILLER</div>
  <div class="badge__role">Manager</div>
  <div class="badge__website">www.brightandtidymn.example</div>
  <div class="badge__brand"><span class="badge__brand-dot"></span><span>Bright and Tidy</span></div>
</div>

<div class="badge badge--back">
  <svg class="badge__art" viewBox="0 0 425 675">
    <defs>
      <linearGradient id="blueBack" x1="0" x2="1" y1="0" y2="0">
        <stop offset="0" stop-color="var(--blue-light)"/>
        <stop offset="1" stop-color="var(--blue-dark)"/>
      </linearGradient>
      <linearGradient id="greenBack" x1="0" x2="1" y1="0" y2="0">
        <stop offset="0" stop-color="var(--green-light)"/>
        <stop offset="1" stop-color="var(--green-bright)"/>
      </linearGradient>
      <linearGradient id="ringBack" x1="0" x2="1" y1="0" y2="1">
        <stop offset="0" stop-color="var(--blue-light)"/>
        <stop offset="1" stop-color="var(--blue-dark)"/>
      </linearGradient>
    </defs>
    <rect class="band-blue" width="425" height="460" fill="url(#blueBack)"/>
    <path class="band-green" d="M0 370 Q120 395 212 330 Q300 270 425 320 L425 460 L0 460 Z" fill="url(#greenBack)"/>
    <path class="band-white" d="M0 450 Q200 300 425 420 L425 675 L0 675 Z" fill="var(--card-bg)"/>
    <circle class="photo-frame" cx="212" cy="300" r="142" fill="var(--card-bg)"/>
    <circle class="photo-ring" cx="212" cy="300" r="136" fill="url(#ringBack)"/>
    <circle class="photo-slot" cx="212" cy="300" r="120" fill="#d9d9d9" role="img" aria-label="Employee portrait photo"/>
    <g class="check-seal" role="img" aria-label="Background check cleared seal">
      <circle cx="342" cy="605" r="42" fill="var(--seal-gold)"/>
      <circle cx="342" cy="605" r="33" fill="var(--seal-dark)"/>
    </g>
  </svg>
  <div class="badge__name">DANA MILLER</div>
  <div class="badge__role">Manager</div>
  <div class="badge__website">www.brightandtidymn.example</div>
  <div class="badge__brand"><span class="badge__brand-dot"></span><span>Bright and Tidy</span></div>
</div>

</body>
</html>
```